Business Card Design Project

We need a business card for a new technology services company. We develop software and implement software packages for our business customers and although we will begin with just one or two service offerings, our service offerings will expand over time. Our name comes from the an author, RK Bellowes, and his "idea" was that opportunity should be based on ability and achievement, not on social status.

We would like to see a design that is standard in its size and shape, but stands apart in its dramatic color contrasts. The card should not use too many colors - the colors used in the background should highlight the brilliant blues of the logo (see attachment) to dramatic effect. The background should not be white.

If necessary, you can change the color of the words "RK Bellowes", but not the word "Idea".

Card size should be U.S. standard 2 inches by 3.5 inches and provide for 1/8 inch bleed area on each side.

We need a design for both sides of the business card, one side communicating the company logo and contact information, the other side being purely graphical, incorporating the logo but no other information.

Contact Information Required:
Mark Linden
MarkLinden@rkbellowesidea.com
555-304-7812

Target Market(s)

Business executives

Industry/Entity Type

Software

Requirements
Must have
• It must have the full company logo on one side, and at least the graphic element of the logo on the other. Either that or the full logo on both.
Nice to have
• It would be nice to have a design that could work without needing two different textures. For example, it would be nice if the entire card could be shiny, not just parts of the card.

It would also be nice if texture is something we could add later.
Should not have
• The card should not use the color green.

```html
<!DOCTYPE html>
<html lang="en">
<head>
<meta charset="utf-8">
<title>RK Bellowes Idea – Business Card</title>
<link href="https://fonts.googleapis.com/css2?family=Open+Sans:wght@400;600;700&display=swap" rel="stylesheet">
<style>
  :root {
    --page: #ffffff;
    --card-dark: #1e1e1f;
    --card-mid: #333334;
    --brand-blue: #0096d6;
    --blue-deep: #0a6fae;
    --blue-bright: #00a8e6;
    --wordmark-grey: #a7a9ac;
    --panel-grey: #a6a8ab;
    --ink-dark: #3a3a3c;
    --white: #ffffff;
  }
  * { margin: 0; padding: 0; box-sizing: border-box; }
  html, body {
    width: 1200px; height: 1000px; overflow: hidden;
    background: var(--page);
    font-family: "Open Sans", Arial, sans-serif;
  }
  .card {
    position: absolute;
    left: 285px; width: 646px; height: 369px;
    overflow: hidden;
    box-shadow: 3px 4px 6px rgba(0,0,0,0.35);
  }
  .card--front {
    top: 111px;
    background: linear-gradient(120deg, var(--card-dark) 0%, var(--card-mid) 60%, #2e2e2f 100%);
  }
  .card--back {
    top: 541px;
    background: linear-gradient(90deg, #373738 0%, #2e2e2f 50%, var(--card-dark) 100%);
  }
  .brand-graphic {
    position: absolute; left: 0; top: 0; width: 360px; height: 300px;
    background: radial-gradient(ellipse at 30% 40%, rgba(0,150,214,0.10) 0%, rgba(0,0,0,0) 70%);
  }
  .wordmark {
    position: absolute;
    display: flex; align-items: center; gap: 10px;
    color: var(--wordmark-grey);
    font-weight: 400;
    letter-spacing: -1.5px;
    white-space: nowrap;
  }
  .wordmark__dot {
    display: inline-block; border-radius: 50%;
    background: var(--brand-blue);
  }
  .card--front .wordmark { right: 38px; top: 285px; font-size: 42px; }
  .card--front .wordmark__dot { width: 22px; height: 22px; }
  .card--back .wordmark { left: 208px; top: 126px; font-size: 36px; }
  .card--back .wordmark__dot { width: 20px; height: 20px; }
  .name-band {
    position: absolute; left: 0; top: 245px; width: 296px; height: 85px;
    background: linear-gradient(90deg, var(--blue-deep) 0%, var(--blue-bright) 100%);
  }
  .name-band__name {
    position: absolute; left: 62px; top: 26px;
    color: var(--white); font-size: 23px; font-weight: 600;
  }
  .contact-panel {
    position: absolute; left: 303px; top: 245px; width: 343px; height: 85px;
    background: var(--panel-grey);
  }
  .contact-list { list-style: none; position: absolute; left: 48px; top: 8px; }
  .contact-list li {
    display: flex; align-items: center; gap: 7px;
    height: 22px;
    color: var(--ink-dark); font-size: 15px;
  }
  .contact-list svg { width: 16px; height: 16px; margin-left: -21px; fill: var(--blue-deep); }
</style>
</head>
<body>

<section class="card card--front" aria-label="Card front">
  <div class="brand-graphic" role="img" aria-label="Brand graphic area"></div>
  <div class="wordmark">RK Bellowes Idea <span class="wordmark__dot"></span></div>
</section>

<section class="card card--back" aria-label="Card back">
  <div class="wordmark">RK Bellowes Idea <span class="wordmark__dot"></span></div>

  <div class="name-band">
    <p class="name-band__name">Mark Linden</p>
  </div>

  <div class="contact-panel">
    <ul class="contact-list">
      <li>
        <svg viewBox="0 0 16 16" aria-hidden="true"><path d="M3.5 1.5 6 4.2 4.8 6c.8 1.9 2.3 3.4 4.2 4.2L10.8 9l2.7 2.5-1.3 2.3c-5.3-.4-9.6-4.7-10-10z"/></svg>
        555-304-7812
      </li>
      <li>
        <svg viewBox="0 0 16 16" aria-hidden="true"><path d="M1 3.5h14v9H1z"/><path d="M1.5 4 8 9l6.5-5" fill="none" stroke="#a6a8ab" stroke-width="1.2"/></svg>
        MarkLinden@rkbellowesidea.com
      </li>
      <li>
        <svg viewBox="0 0 16 16" aria-hidden="true"><circle cx="8" cy="8" r="6.5" fill="none" stroke="#0a6fae" stroke-width="1.3"/><ellipse cx="8" cy="8" rx="2.8" ry="6.5" fill="none" stroke="#0a6fae" stroke-width="1.1"/><path d="M1.5 8h13M2.5 5h11M2.5 11h11" stroke="#0a6fae" stroke-width="1"/></svg>
        www.rkbellowesidea.com
      </li>
    </ul>
  </div>
</section>

</body>
</html>
```